3 Months free alarm monitoring from TK Guardline Ltd

We are offering 3 months monitoring free to every new connection when you sign a 12 monitoring contract. Prices start at $25incl GST for our standard service. No phoneline? No Problem! Ask about our GPRS monitoring service through the Telvarra Network. A one off connection fee of $65incl GST for our standard service applies.

Double sided colour.

3 months free alarm monitoring offer on the front.

Terms and standard pricing on the back.

Other services we offer: to be on the back
Alarm systems/servicing
CCTV systems
Intercom systems
Access control systems

TK Guardline Ltd
www.tkguardline.co.nz
monitoring@tkguardline.co.nz
094637158
0215876102

Target Market(s)

Residential and commercial

Industry/Entity Type

Security

Font styles to use
Serif
Sans Serif

Requirements
Must have
• On the front:
• Limited time offer.
• 3 Months free alarm monitoring.
• TK Guardline Ltd
• www.tkguardline.co.nz
• monitoring@tkguardline.co.nz
• 094637158
• 0215876102
• Images similar to the files.
• On the back:
• At the top:
• No phoneline? Naked broadband? Voip?
• No problem! Ask about our monitoring solutions through the Telvarra GPRS Network.
• Lintrova logo.
• In the middle:
• Other services we offer:
• Alarm systems & servicing
• CCTV systems
• Intercoms
• Access control systems
• At the bottom:
• 3 free months monitoring when you sign a 12month contract. $65 one off setup fee applies. Monitoring plans from $25/month for our standard service. Other plans available please feel free to contact us to discuss your requirements.
Nice to have
• Check the business card file for the style I am after.

```html
<!DOCTYPE html>
<html lang="en">
<head>
<meta charset="utf-8">
<title>TK Guardline Ltd – Alarm Monitoring Flyer</title>
<link href="https://fonts.googleapis.com/css2?family=Oswald:wght@500;700&family=Open+Sans:wght@400;600;700&display=swap" rel="stylesheet">
<style>
  :root{
    --navy:#0b2363;
    --blue:#1c4eb0;
    --blue-light:#3f78d6;
    --red:#d7202a;
    --grey:#b9bec8;
    --white:#ffffff;
    --ink:#1d2433;
    --page:#eef0f3;
  }
  *{box-sizing:border-box;margin:0;padding:0}
  html,body{width:878px;height:1200px;overflow:hidden;background:var(--page)}
  body{font-family:"Open Sans",Arial,sans-serif;color:var(--ink);position:relative}

  .flyer{position:absolute;left:12px;width:854px;height:580px;overflow:hidden;background:var(--navy);box-shadow:0 2px 6px rgba(0,0,0,.2)}
  .flyer--front{top:12px}
  .flyer--back{top:608px}
  .flyer__bg{position:absolute;inset:0;width:100%;height:100%}

  .brand{position:absolute;right:30px;top:34px;width:330px}
  .brand__name{display:flex;align-items:center;gap:12px;font-family:"Oswald",sans-serif;font-weight:700;font-size:30px;color:var(--navy);line-height:1;letter-spacing:.5px;white-space:nowrap}
  .brand__mark{width:42px;height:42px;border-radius:50%;background:var(--red);flex:none}
  .contacts{list-style:none;margin-top:12px;padding-left:54px}
  .contacts li{display:flex;align-items:center;gap:8px;font-weight:700;font-size:15px;color:var(--red);line-height:1.55;white-space:nowrap}
  .contacts li.small{font-size:11.5px;font-weight:600;color:var(--ink)}
  .contacts .icon{width:16px;height:16px;border-radius:50%;background:var(--red);display:flex;align-items:center;justify-content:center;flex:none}
  .contacts .icon svg{width:10px;height:10px;fill:var(--white)}

  .offer{position:absolute;left:28px;top:170px}
  .offer__three{position:absolute;left:0;top:0;font-family:"Oswald",sans-serif;font-weight:700;font-size:230px;line-height:.8;color:var(--red);-webkit-text-stroke:5px var(--white);paint-order:stroke fill;transform:skewX(-6deg)}
  .offer__words{position:absolute;left:128px;top:10px;font-family:"Oswald",sans-serif;font-weight:700;color:var(--white);line-height:.92;transform:skewX(-6deg)}
  .offer__months{font-size:70px;display:block}
  .offer__free{font-size:104px;display:block;color:var(--red);-webkit-text-stroke:4px var(--white);paint-order:stroke fill}
  .banner{position:absolute;left:0;height:58px;display:flex;align-items:center;padding-left:30px;background:var(--red);color:var(--white);font-family:"Oswald",sans-serif;font-weight:700;white-space:nowrap;clip-path:polygon(0 0,100% 0,calc(100% - 22px) 100%,0 100%)}
  .banner--offer{top:398px;width:440px;font-size:40px}
  .limited{position:absolute;left:34px;top:474px;color:var(--white);font-size:24px}
  .photo{position:absolute}
  .photo--remote{left:498px;top:220px;width:320px;height:320px;border-radius:50%;border:6px solid var(--white);background:radial-gradient(circle at 60% 40%,#c9b79a,#7a6a55 55%,#3b3a44)}

  .pitch__q{position:absolute;left:30px;top:34px;color:var(--white);font-family:"Oswald",sans-serif;font-weight:700;font-size:36px;line-height:1.08}
  .banner--problem{top:160px;width:350px;font-size:40px;height:54px}
  .pitch__text{position:absolute;left:30px;top:226px;width:370px;color:var(--white);font-size:17px;line-height:1.35}
  .banner--services{top:300px;width:300px;height:auto;padding:5px 30px 7px;font-size:24px;line-height:1.05;display:block}
  .services{position:absolute;left:32px;top:368px;list-style:none;color:var(--white);font-size:16px;line-height:1.6}
  .services li{display:flex;align-items:center;gap:10px}
  .services svg{width:16px;height:16px;flex:none}
  .terms{position:absolute;left:30px;top:508px;width:800px;color:var(--white);font-size:14px;font-weight:700;line-height:1.3}
  .terms__note{position:absolute;left:30px;top:552px;color:var(--white);font-size:11px}
  .photo--devices{left:470px;top:222px;width:360px;height:262px;border-radius:8px;background:linear-gradient(135deg,#2b2f3a,#6d7380 45%,#d7dae0)}
</style>
</head>
<body>

<section class="flyer flyer--front">
  <svg class="flyer__bg" viewBox="0 0 854 580" preserveAspectRatio="none" aria-hidden="true">
    <defs>
      <radialGradient id="frontGlow" cx="0.3" cy="0.45" r="0.7">
        <stop offset="0" stop-color="#3f78d6"/>
        <stop offset="1" stop-color="#0b2363"/>
      </radialGradient>
    </defs>
    <rect width="854" height="580" fill="url(#frontGlow)"/>
    <path d="M400 0 C480 250 660 460 854 540 L854 0 Z" fill="#ffffff"/>
    <path d="M380 0 C470 260 650 470 854 555" fill="none" stroke="#b9bec8" stroke-width="18"/>
    <path d="M350 0 C450 280 640 490 854 575" fill="none" stroke="#d7202a" stroke-width="26"/>
    <path d="M320 0 C430 300 620 510 820 580" fill="none" stroke="#1c4eb0" stroke-width="14"/>
  </svg>

  <div class="brand">
    <div class="brand__name"><span class="brand__mark"></span>TK GUARDLINE LTD</div>
    <ul class="contacts">
      <li><span class="icon"><svg viewBox="0 0 24 24"><path d="M6.6 10.8a15 15 0 006.6 6.6l2.2-2.2a1 1 0 011-.25 11 11 0 003.6.6 1 1 0 011 1V20a1 1 0 01-1 1A17 17 0 013 4a1 1 0 011-1h3.5a1 1 0 011 1 11 11 0 00.6 3.6 1 1 0 01-.25 1z"/></svg></span>094637158</li>
      <li><span class="icon"><svg viewBox="0 0 24 24"><path d="M7 1h10a2 2 0 012 2v18a2 2 0 01-2 2H7a2 2 0 01-2-2V3a2 2 0 012-2zm0 3v14h10V4z"/></svg></span>0215876102</li>
      <li class="small"><span class="icon"><svg viewBox="0 0 24 24"><path d="M2 5h20v14H2zm2 2v.5l8 5 8-5V7z"/></svg></span>monitoring@tkguardline.co.nz</li>
      <li class="small"><span class="icon"><svg viewBox="0 0 24 24"><circle cx="12" cy="12" r="9"/></svg></span>www.tkguardline.co.nz</li>
    </ul>
  </div>

  <div class="offer">
    <span class="offer__three">3</span>
    <div class="offer__words">
      <span class="offer__months">MONTHS</span>
      <span class="offer__free">FREE</span>
    </div>
  </div>
  <div class="banner banner--offer">ALARM MONITORING</div>
  <p class="limited">Limited time offer</p>

  <div class="photo photo--remote" role="img" aria-label="Hand holding an alarm remote in front of a two-storey house"></div>
</section>

<section class="flyer flyer--back">
  <svg class="flyer__bg" viewBox="0 0 854 580" preserveAspectRatio="none" aria-hidden="true">
    <defs>
      <radialGradient id="backGlow" cx="0.25" cy="0.5" r="0.8">
        <stop offset="0" stop-color="#3f78d6"/>
        <stop offset="1" stop-color="#0b2363"/>
      </radialGradient>
    </defs>
    <rect width="854" height="580" fill="url(#backGlow)"/>
    <path d="M440 0 C430 180 440 380 460 500 L854 500 L854 0 Z" fill="#ffffff"/>
    <path d="M420 0 C410 180 420 380 440 500" fill="none" stroke="#b9bec8" stroke-width="14"/>
    <path d="M400 0 C390 180 400 380 420 500" fill="none" stroke="#d7202a" stroke-width="20"/>
    <rect y="498" width="854" height="82" fill="#0b2363"/>
  </svg>

  <p class="pitch__q">NO PHONELINE?<br>NAKED BROADBAND?<br>VOIP?</p>
  <div class="banner banner--problem">NO PROBLEM!</div>
  <p class="pitch__text">Ask about our monitoring solutions through the Telvarra GPRS Network.</p>
  <div class="banner banner--services">OTHER SERVICES<br>WE OFFER</div>
  <ul class="services">
    <li><svg viewBox="0 0 24 24"><rect width="24" height="24" rx="4" fill="#d7202a"/><path d="M6 12l4 4 8-8" stroke="#fff" stroke-width="3" fill="none"/></svg>Alarm systems &amp; servicing</li>
    <li><svg viewBox="0 0 24 24"><rect width="24" height="24" rx="4" fill="#d7202a"/><path d="M6 12l4 4 8-8" stroke="#fff" stroke-width="3" fill="none"/></svg>CCTV systems</li>
    <li><svg viewBox="0 0 24 24"><rect width="24" height="24" rx="4" fill="#d7202a"/><path d="M6 12l4 4 8-8" stroke="#fff" stroke-width="3" fill="none"/></svg>Intercoms</li>
    <li><svg viewBox="0 0 24 24"><rect width="24" height="24" rx="4" fill="#d7202a"/><path d="M6 12l4 4 8-8" stroke="#fff" stroke-width="3" fill="none"/></svg>Access control systems</li>
  </ul>

  <div class="brand">
    <div class="brand__name"><span class="brand__mark"></span>TK GUARDLINE LTD</div>
    <ul class="contacts">
      <li><span class="icon"><svg viewBox="0 0 24 24"><path d="M6.6 10.8a15 15 0 006.6 6.6l2.2-2.2a1 1 0 011-.25 11 11 0 003.6.6 1 1 0 011 1V20a1 1 0 01-1 1A17 17 0 013 4a1 1 0 011-1h3.5a1 1 0 011 1 11 11 0 00.6 3.6 1 1 0 01-.25 1z"/></svg></span>094637158</li>
      <li><span class="icon"><svg viewBox="0 0 24 24"><path d="M7 1h10a2 2 0 012 2v18a2 2 0 01-2 2H7a2 2 0 01-2-2V3a2 2 0 012-2zm0 3v14h10V4z"/></svg></span>0215876102</li>
      <li class="small"><span class="icon"><svg viewBox="0 0 24 24"><path d="M2 5h20v14H2zm2 2v.5l8 5 8-5V7z"/></svg></span>monitoring@tkguardline.co.nz</li>
      <li class="small"><span class="icon"><svg viewBox="0 0 24 24"><circle cx="12" cy="12" r="9"/></svg></span>www.tkguardline.co.nz</li>
    </ul>
  </div>

  <div class="photo photo--devices" role="img" aria-label="Alarm keypad, smartphone with home monitoring app and key fob remotes"></div>

  <p class="terms">3 free months monitoring when you sign a 12 month contract. $65 connection fee applies. Monitoring plans from $25/month for our standard service.</p>
  <p class="terms__note">Other plans available please feel free to contact us to discuss your requirements.</p>
</section>

</body>
</html>
```